Personal informs intake and New Zealand divorce form automated filling service

I need a website that has a professional appearance, take information from clients, automatically fill New Zealand divorce forms based on information gathered. The personal information are listed:
Applicant’s information

1 First name

2 Middle name ( if Any )

3 Last name

4 Date of birth

5 Address

6 Email

7 Gender

8 Mobile

9 Occupation

10 Ethnicity

11 Country of residence

12 Do you live in New Zealand permanently?

13 Do you and your spouse have children who are under age 16 who require additional care?

Spouse’s information

1 Spouse’s first name

2 Spouse’s middle name ( if any )

3 Spouse’s last name

4 Spouse’s date of birth

5 Spouse’s occupation

6 Spouse’s ethnicity

7 Mobil number

8 Address

Marriage details

1 Did either party change their name by deed poll following the marriage/ civil union.

2 Date of marriage

3 Place and Address where the marriage was solemnized?

4 What date did you start living together?

5 What date did you cease living together?

6 How did you agree to separate? ( verbal agreement, written agreement, court order, or other )

The forms are New Zealand one party/joint application for Order dissolving a marriage or civil union.
Once the forms are completed, it will be checked by a human before sending to the paid clients by email. The website needs to integrate multiple mainstream payment options.

The forms are uploaded, please view it and set up the questionnaire accordingly to ensure all questions in the forms are answered. Must be able to distinguish one party or joint application.

Please contact me if you are interested and need more information.

Updated an AI generated draft as a sample

Target Market(s)

Divorcées

Coding

Coded - Design and coding required

Number of Pages Required

1 page

Font styles to use
Sans Serif

Colors

Designer to choose colors to be used in the design.

Requirements
Must have
• A professional appearance, easy to initiate the information intake process
Nice to have
• Step by step guideline, easy to understand how the website works
Should not have
• Bright colors

```html
<!DOCTYPE html>
<html lang="en">
<head>
<meta charset="utf-8">
<title>Divorce Application Intake – Family Records Office</title>
<link rel="stylesheet" href="https://fonts.googleapis.com/css2?family=Plus+Jakarta+Sans:wght@400;500;600&display=swap">
<style>
  :root {
    --ink: #2f3337;
    --muted: #8a9199;
    --brand: #3b9bd8;
    --brand-dark: #1f6fb0;
    --panel: #ebf3fb;
    --field-border: #c7d4e0;
    --cal-bg: #e2eaf2;
    --track: #d9dde2;
    --bar: #000000;
    --page: #ffffff;
  }
  * { box-sizing: border-box; margin: 0; padding: 0; }
  html, body { width: 1200px; height: 786px; overflow: hidden; background: var(--page); }
  body { font-family: "Plus Jakarta Sans", Arial, sans-serif; color: var(--ink); }

  .stage { position: absolute; left: 0; top: 0; width: 2376px; height: 1556px; transform: scale(0.50505); transform-origin: 0 0; }
  .screen { position: absolute; top: 48px; width: 700px; height: 1458px; background: var(--page); box-shadow: 0 0 0 1px #f0f0f0; }
  .screen > * { position: absolute; }

  .topbar { left: 0; top: 0; width: 700px; height: 62px; background: var(--bar); display: flex; align-items: center; justify-content: center; }
  .brand { display: flex; align-items: center; gap: 8px; height: 32px; }
  .brand-square { width: 22px; height: 32px; background: var(--brand); }
  .brand-name { color: #ffffff; font-size: 13px; font-weight: 600; letter-spacing: .5px; }

  .footer { left: 0; top: 1397px; width: 700px; height: 61px; background: var(--bar); color: #fff; font-size: 16px; font-weight: 500; display: flex; align-items: center; justify-content: center; }

  .step { top: 93px; font-size: 10px; color: var(--ink); white-space: nowrap; }
  .step.active { top: 89px; font-size: 15px; font-weight: 600; color: var(--brand); }
  .track { left: 65px; top: 127px; width: 570px; height: 2px; background: var(--track); }
  .track-fill { left: 65px; top: 127px; height: 2px; background: var(--brand); }
  .dot { top: 124px; width: 8px; height: 8px; border-radius: 50%; background: var(--brand); margin-left: -4px; }
  .dot.off { background: var(--track); }

  .title { left: 0; width: 700px; top: 170px; text-align: center; font-size: 19px; font-weight: 500; }

  .panel { left: 65px; width: 570px; background: var(--panel); }
  .label { font-size: 12.5px; line-height: 19px; color: var(--ink); }
  .label small { font-size: 12.5px; color: #555; }
  .field { height: 22px; background: #fff; border: 1px solid var(--field-border); }
  .field.wide { width: 318px; }
  .field.half { width: 146px; }
  .field.box { width: 146px; height: 46px; }
  .prefix { font-size: 9px; color: var(--brand); padding: 5px 9px; }
  .prefix::after { content: ""; display: inline-block; width: 1px; height: 10px; background: var(--field-border); margin-left: 5px; vertical-align: middle; }
  .select::after { content: ""; position: absolute; right: 10px; top: 9px; border: 2.5px solid transparent; border-top: 3px solid var(--brand); }

  .radio { display: flex; align-items: center; gap: 8px; font-size: 9px; color: var(--ink); }
  .radio i { width: 16px; height: 16px; border-radius: 50%; background: #fff; border: 1px solid var(--field-border); display: flex; align-items: center; justify-content: center; }
  .radio.on i::after { content: ""; width: 6px; height: 6px; border-radius: 50%; background: var(--brand); }

  .cal { width: 146px; height: 166px; border: 1px solid #a9c2d8; background: var(--cal-bg); }
  .cal-head { height: 22px; background: #fff; border-bottom: 1px solid #c7d4e0; display: flex; align-items: center; justify-content: space-between; padding: 0 8px 0 11px; font-size: 8.5px; color: var(--brand); }
  .cal-month { font-size: 8px; padding: 11px 0 0 11px; color: var(--ink); }
  .cal-month::after { content: ""; display: inline-block; margin-left: 6px; border: 2.5px solid transparent; border-top: 3px solid var(--ink); vertical-align: -1px; }
  .cal-grid { display: grid; grid-template-columns: repeat(7, 19px); grid-auto-rows: 15px; padding: 8px 0 0 5px; font-size: 7px; text-align: center; align-items: center; justify-items: center; }
  .cal-grid b { font-weight: 600; }
  .cal-grid .today { width: 12px; height: 12px; line-height: 12px; border-radius: 50%; background: var(--brand); color: #fff; }

  .btn { left: 255px; width: 180px; height: 32px; font-size: 12.5px; display: flex; align-items: center; justify-content: center; }
  .btn.primary { background: var(--brand); color: #fff; }
  .btn.ghost { background: #fff; border: 1px solid #9aa2aa; color: var(--muted); }
  .rule { left: 255px; width: 180px; height: 1px; background: #dde1e5; }
  .note { left: 0; width: 700px; text-align: center; font-size: 12px; line-height: 19px; color: var(--muted); }
</style>
</head>
<body>
<div class="stage">

  <!-- Step 1: Applicant -->
  <section class="screen" style="left:63px">
    <header class="topbar"><div class="brand"><span class="brand-square"></span><span class="brand-name">FAMILY RECORDS OFFICE</span></div></header>
    <span class="step active" style="left:66px">Applicant’s information</span>
    <span class="step" style="left:299px">Spouse’s information</span>
    <span class="step" style="left:536px">Marriage Details</span>
    <div class="track"></div><div class="track-fill" style="width:78px"></div>
    <span class="dot" style="left:143px"></span><span class="dot" style="left:350px"></span><span class="dot off" style="left:578px"></span>
    <h1 class="title">Please Fill in Applicant’s Information</h1>

    <div class="panel" style="top:223px;height:219px"></div>
    <span class="label" style="left:189px;top:243px">First name</span>
    <div class="field wide" style="left:189px;top:269px"></div>
    <span class="label" style="left:189px;top:304px">Middle name <small>(if any)</small></span>
    <div class="field wide" style="left:189px;top:330px"></div>
    <span class="label" style="left:189px;top:366px">Last name</span>
    <div class="field wide" style="left:189px;top:392px"></div>

    <div class="panel" style="top:464px;height:242px"></div>
    <span class="label" style="left:189px;top:486px">Date of Birth</span>
    <div class="cal" style="left:189px;top:513px">
      <div class="cal-head">Select a date<svg width="10" height="10" viewBox="0 0 10 10"><rect x="1" y="2" width="8" height="7" fill="none" stroke="#3b9bd8"/><line x1="1" y1="4.5" x2="9" y2="4.5" stroke="#3b9bd8"/><line x1="3" y1="0.5" x2="3" y2="2.5" stroke="#3b9bd8"/><line x1="7" y1="0.5" x2="7" y2="2.5" stroke="#3b9bd8"/></svg></div>
      <div class="cal-month">April 2003</div>
      <div class="cal-grid"><b>M</b><b>T</b><b>W</b><b>T</b><b>F</b><b>S</b><b>S</b><span>1</span><span>2</span><span>3</span><span>4</span><span>5</span><span>6</span><span>7</span><span>8</span><span>9</span><span>10</span><span>11</span><span>12</span><span>13</span><span>14</span><span>15</span><span>16</span><span class="today">17</span><span>18</span><span>19</span><span>20</span><span>21</span><span>22</span><span>23</span><span>24</span><span>25</span><span>26</span><span>27</span><span>28</span><span>29</span><span>30</span></div>
    </div>
    <span class="label" style="left:362px;top:486px">Address</span>
    <div class="field box" style="left:362px;top:513px"></div>
    <span class="label" style="left:362px;top:571px">Email</span>
    <div class="field half" style="left:362px;top:598px"></div>
    <span class="label" style="left:362px;top:633px">Gender</span>
    <span class="radio on" style="left:362px;top:663px"><i></i>Male</span>
    <span class="radio" style="left:426px;top:663px"><i></i>Female</span>

    <div class="panel" style="top:728px;height:160px"></div>
    <span class="label" style="left:189px;top:746px">Mobile</span>
    <div class="field half" style="left:189px;top:773px"><div class="prefix">027 +</div></div>
    <span class="label" style="left:363px;top:746px">Occupation</span>
    <div class="field half" style="left:362px;top:773px"></div>
    <span class="label" style="left:189px;top:810px">Ethnicity</span>
    <div class="field half select" style="left:189px;top:837px;position:absolute"></div>
    <span class="label" style="left:362px;top:810px">Country of residence</span>
    <div class="field half select" style="left:362px;top:837px;position:absolute"></div>

    <div class="panel" style="top:911px;height:174px"></div>
    <span class="label" style="left:189px;top:934px">Do you live in New Zealand permanently?</span>
    <span class="radio on" style="left:189px;top:963px"><i></i>Yes</span>
    <span class="radio" style="left:253px;top:963px"><i></i>No</span>
    <span class="label" style="left:189px;top:994px;width:330px">Do you and your spouse have children who are under age 16 who require additional care?</span>
    <span class="radio on" style="left:189px;top:1041px"><i></i>Yes</span>
    <span class="radio" style="left:253px;top:1041px"><i></i>No</span>

    <span class="btn primary" style="top:1126px">Continue</span>
    <span class="btn ghost" style="top:1167px">Back</span>
    <p class="note" style="top:1228px">Please ensure all questions in<br>the form are answered.</p>
    <footer class="footer">New Zealand Divorce - Family Records Office</footer>
  </section>

  <!-- Step 2: Spouse -->
  <section class="screen" style="left:840px">
    <header class="topbar"><div class="brand"><span class="brand-square"></span><span class="brand-name">FAMILY RECORDS OFFICE</span></div></header>
    <span class="step" style="left:66px">Applicant’s information</span>
    <span class="step active" style="left:278px">Spouse’s information</span>
    <span class="step" style="left:536px">Marriage Details</span>
    <div class="track"></div><div class="track-fill" style="width:285px"></div>
    <span class="dot" style="left:123px"></span><span class="dot" style="left:350px"></span><span class="dot off" style="left:575px"></span>
    <h1 class="title">Please Fill in Spouse’s Information</h1>

    <div class="panel" style="top:223px;height:219px"></div>
    <span class="label" style="left:189px;top:243px">Spouse’s First name</span>
    <div class="field wide" style="left:189px;top:269px"></div>
    <span class="label" style="left:189px;top:304px">Spouse’s Middle name <small>(if any)</small></span>
    <div class="field wide" style="left:189px;top:330px"></div>
    <span class="label" style="left:189px;top:366px">Spouse’s Last name</span>
    <div class="field wide" style="left:189px;top:392px"></div>

    <div class="panel" style="top:464px;height:242px"></div>
    <span class="label" style="left:189px;top:486px">Spouse’s Date of Birth</span>
    <div class="cal" style="left:189px;top:513px">
      <div class="cal-head">Select a date<svg width="10" height="10" viewBox="0 0 10 10"><rect x="1" y="2" width="8" height="7" fill="none" stroke="#3b9bd8"/><line x1="1" y1="4.5" x2="9" y2="4.5" stroke="#3b9bd8"/><line x1="3" y1="0.5" x2="3" y2="2.5" stroke="#3b9bd8"/><line x1="7" y1="0.5" x2="7" y2="2.5" stroke="#3b9bd8"/></svg></div>
      <div class="cal-month">April 2003</div>
      <div class="cal-grid"><b>M</b><b>T</b><b>W</b><b>T</b><b>F</b><b>S</b><b>S</b><span>1</span><span>2</span><span>3</span><span>4</span><span>5</span><span>6</span><span>7</span><span>8</span><span>9</span><span>10</span><span>11</span><span>12</span><span>13</span><span>14</span><span>15</span><span>16</span><span class="today">17</span><span>18</span><span>19</span><span>20</span><span>21</span><span>22</span><span>23</span><span>24</span><span>25</span><span>26</span><span>27</span><span>28</span><span>29</span><span>30</span></div>
    </div>
    <span class="label" style="left:362px;top:486px">Spouse’s Address</span>
    <div class="field box" style="left:362px;top:513px"></div>
    <span class="label" style="left:362px;top:569px">Mobile Number</span>
    <div class="field half" style="left:362px;top:596px"><div class="prefix">027 +</div></div>

    <div class="panel" style="top:728px;height:92px"></div>
    <span class="label" style="left:189px;top:746px">Ethnicity</span>
    <div class="field half select" style="left:189px;top:773px;position:absolute"></div>
    <span class="label" style="left:363px;top:746px">Occupation</span>
    <div class="field half" style="left:362px;top:773px"></div>

    <span class="btn primary" style="top:869px">Continue</span>
    <span class="btn ghost" style="top:910px">Back</span>
    <span class="rule" style="top:959px"></span>
    <p class="note" style="top:972px">Please ensure all questions in<br>the form are answered.</p>
    <footer class="footer">New Zealand Divorce - Family Records Office</footer>
  </section>

  <!-- Step 3: Marriage -->
  <section class="screen" style="left:1603px">
    <header class="topbar"><div class="brand"><span class="brand-square"></span><span class="brand-name">FAMILY RECORDS OFFICE</span></div></header>
    <span class="step" style="left:65px">Applicant’s information</span>
    <span class="step" style="left:298px">Spouse’s information</span>
    <span class="step active" style="left:525px">Marriage Details</span>
    <div class="track"></div><div class="track-fill" style="width:512px"></div>
    <span class="dot" style="left:143px"></span><span class="dot" style="left:350px"></span><span class="dot" style="left:577px"></span>
    <h1 class="title">Please Fill in Marriage Details</h1>

    <div class="panel" style="top:223px;height:317px"></div>
    <span class="label" style="left:189px;top:242px;width:300px">Did either party change their name by deed poll following the marriage/ civil union ?</span>
    <span class="radio on" style="left:189px;top:290px"><i></i>Yes</span>
    <span class="radio" style="left:253px;top:290px"><i></i>No</span>
    <span class="label" style="left:191px;top:322px">Date of marriage</span>
    <div class="cal" style="left:189px;top:349px">
      <div class="cal-head">Select a date<svg width="10" height="10" viewBox="0 0 10 10"><rect x="1" y="2" width="8" height="7" fill="none" stroke="#3b9bd8"/><line x1="1" y1="4.5" x2="9" y2="4.5" stroke="#3b9bd8"/><line x1="3" y1="0.5" x2="3" y2="2.5" stroke="#3b9bd8"/><line x1="7" y1="0.5" x2="7" y2="2.5" stroke="#3b9bd8"/></svg></div>
      <div class="cal-month">April 2003</div>
      <div class="cal-grid"><b>M</b><b>T</b><b>W</b><b>T</b><b>F</b><b>S</b><b>S</b><span>1</span><span>2</span><span>3</span><span>4</span><span>5</span><span>6</span><span>7</span><span>8</span><span>9</span><span>10</span><span>11</span><span>12</span><span>13</span><span>14</span><span>15</span><span>16</span><span class="today">17</span><span>18</span><span>19</span><span>20</span><span>21</span><span>22</span><span>23</span><span>24</span><span>25</span><span>26</span><span>27</span><span>28</span><span>29</span><span>30</span></div>
    </div>
    <span class="label" style="left:362px;top:322px;width:150px">Place and Address where the marriage was solemnized?</span>
    <div class="field box" style="left:362px;top:391px"></div>

    <div class="panel" style="top:562px;height:418px"></div>
    <span class="label" style="left:189px;top:582px;width:150px">What date did you start living together?</span>
    <span class="label" style="left:360px;top:582px;width:160px">What date did you cease living together?</span>
    <div class="cal" style="left:189px;top:637px">
      <div class="cal-head">Select a date<svg width="10" height="10" viewBox="0 0 10 10"><rect x="1" y="2" width="8" height="7" fill="none" stroke="#3b9bd8"/><line x1="1" y1="4.5" x2="9" y2="4.5" stroke="#3b9bd8"/><line x1="3" y1="0.5" x2="3" y2="2.5" stroke="#3b9bd8"/><line x1="7" y1="0.5" x2="7" y2="2.5" stroke="#3b9bd8"/></svg></div>
      <div class="cal-month">April 2003</div>
      <div class="cal-grid"><b>M</b><b>T</b><b>W</b><b>T</b><b>F</b><b>S</b><b>S</b><span>1</span><span>2</span><span>3</span><span>4</span><span>5</span><span>6</span><span>7</span><span>8</span><span>9</span><span>10</span><span>11</span><span>12</span><span>13</span><span>14</span><span>15</span><span>16</span><span class="today">17</span><span>18</span><span>19</span><span>20</span><span>21</span><span>22</span><span>23</span><span>24</span><span>25</span><span>26</span><span>27</span><span>28</span><span>29</span><span>30</span></div>
    </div>
    <div class="cal" style="left:360px;top:637px">
      <div class="cal-head">Select a date<svg width="10" height="10" viewBox="0 0 10 10"><rect x="1" y="2" width="8" height="7" fill="none" stroke="#3b9bd8"/><line x1="1" y1="4.5" x2="9" y2="4.5" stroke="#3b9bd8"/><line x1="3" y1="0.5" x2="3" y2="2.5" stroke="#3b9bd8"/><line x1="7" y1="0.5" x2="7" y2="2.5" stroke="#3b9bd8"/></svg></div>
      <div class="cal-month">April 2003</div>
      <div class="cal-grid"><b>M</b><b>T</b><b>W</b><b>T</b><b>F</b><b>S</b><b>S</b><span>1</span><span>2</span><span>3</span><span>4</span><span>5</span><span>6</span><span>7</span><span>8</span><span>9</span><span>10</span><span>11</span><span>12</span><span>13</span><span>14</span><span>15</span><span>16</span><span class="today">17</span><span>18</span><span>19</span><span>20</span><span>21</span><span>22</span><span>23</span><span>24</span><span>25</span><span>26</span><span>27</span><span>28</span><span>29</span><span>30</span></div>
    </div>
    <span class="label" style="left:189px;top:823px">How did you agree to separate?</span>
    <span class="radio" style="left:189px;top:852px"><i></i>Verbal agreement</span>
    <span class="radio" style="left:360px;top:852px"><i></i>Written agreement</span>
    <span class="radio" style="left:189px;top:881px"><i></i>Court order</span>
    <span class="radio on" style="left:360px;top:881px"><i></i>Other Reason</span>
    <div class="field box" style="left:360px;top:913px"></div>

    <span class="btn primary" style="top:1018px">Submit Form</span>
    <span class="btn ghost" style="top:1059px">Back</span>
    <span class="rule" style="top:1108px"></span>
    <p class="note" style="top:1121px">Please ensure all questions in<br>the form are answered.</p>
    <footer class="footer">New Zealand Divorce - Family Records Office</footer>
  </section>

</div>
</body>
</html>
```